DM - management consultant

Business card - contemporary design

Front info
Dorian Maples

(Address not necessary)
PO Box 7386
Fernvale, CA 94187

(650) 555-0143
dm@dorianmapl.es

Chatline: dmq527
Friendbook: /Dorian.Maples
Workroll: /in/dorianmaples

Back or Front
www.dorianmaples.net
Facilitation & coaching, change management, strategic partnerships, business improvement

Target Market(s)

High tech businesses - mostly startups in Silicon Valley

Industry/Entity Type

Business

Font styles to use
Sans Serif

Colors

Designer to choose colors to be used in the design.

```html
<!DOCTYPE html>
<html lang="en">
<head>
<meta charset="utf-8">
<title>DM-management business card</title>
<link rel="stylesheet" href="https://fonts.googleapis.com/css2?family=Source+Sans+3:wght@400;600;700&display=swap">
<style>
  :root {
    --backdrop: #adabac;
    --card: #ffffff;
    --sky: #56c3f1;
    --sky-text: #3ba3d6;
    --link: #4fc1ef;
    --amber: #f6b125;
    --ink: #1f1f1f;
    --mark-ink: #2a2a2a;
  }
  * { box-sizing: border-box; margin: 0; padding: 0; }
  html, body {
    width: 1200px; height: 900px; overflow: hidden;
    background: var(--backdrop);
    font-family: "Source Sans 3", "Helvetica Neue", Arial, sans-serif;
    color: var(--ink);
  }
  .stage { position: relative; width: 1200px; height: 900px; }
  .card {
    position: absolute;
    background: var(--card);
    border-radius: 24px;
    overflow: hidden;
    box-shadow: 4px 5px 6px rgba(0,0,0,0.35);
  }
  .card--back { left: 18px; top: 342px; width: 566px; height: 328px; }
  .card--front { left: 612px; top: 340px; width: 566px; height: 328px; }

  .side-band {
    position: absolute; left: 0; top: 0; bottom: 0; width: 107px;
    background: var(--sky);
    border-right: 4px solid var(--amber);
  }

  .brand {
    position: absolute;
    display: flex; align-items: center; gap: 10px;
  }
  .brand__square { width: 28px; height: 28px; background: var(--sky); }
  .brand__name {
    font-size: 25px; font-weight: 700; letter-spacing: -0.5px;
    color: var(--mark-ink); white-space: nowrap;
  }
  .card--back .brand { left: 210px; top: 150px; }
  .card--front .brand { left: 312px; top: 246px; }

  .website {
    position: absolute; left: 219px; top: 185px;
    font-size: 16px; color: var(--link);
  }

  .services {
    position: absolute; left: 124px; top: 262px;
    display: grid; grid-template-columns: 201px 201px; row-gap: 3px;
    list-style: none; font-size: 17px;
  }
  .services li { position: relative; padding-left: 20px; line-height: 18px; white-space: nowrap; }
  .services li::before {
    content: ""; position: absolute; left: 0; top: 5px;
    width: 10px; height: 10px; border-radius: 50%; background: var(--amber);
  }

  .person { position: absolute; left: 36px; top: 48px; }
  .person__name { font-size: 23px; font-weight: 400; color: var(--sky-text); line-height: 26px; }
  .person__title { font-size: 16px; line-height: 18px; }

  .address { position: absolute; left: 36px; top: 128px; font-size: 16px; line-height: 20px; font-style: normal; }

  .contact { position: absolute; left: 36px; top: 190px; font-size: 16px; line-height: 20px; list-style: none; }
  .contact li { display: flex; align-items: center; gap: 5px; }
  .contact svg { width: 11px; height: 11px; fill: var(--amber); }

  .social { position: absolute; left: 35px; top: 234px; font-size: 16px; line-height: 21px; list-style: none; }
  .social__label { color: var(--sky-text); }
</style>
</head>
<body>
<main class="stage">

  <section class="card card--back" aria-label="Card back">
    <div class="side-band"></div>
    <div class="brand">
      <span class="brand__square"></span>
      <span class="brand__name">DM - management</span>
    </div>
    <p class="website">www.dorianmaples.net</p>
    <ul class="services">
      <li>Facilitation &amp; coaching</li>
      <li>change management</li>
      <li>strategic partnerships</li>
      <li>business improvement</li>
    </ul>
  </section>

  <section class="card card--front" aria-label="Card front">
    <div class="person">
      <h1 class="person__name">Dorian Maples</h1>
      <p class="person__title">title here</p>
    </div>
    <address class="address">
      PO Box 7386<br>Fernvale, CA 94187
    </address>
    <ul class="contact">
      <li>
        <svg viewBox="0 0 12 12" aria-hidden="true"><path d="M1 4c0-2 1-3 5-3s5 1 5 3v1H8V4H4v1H1z M3 6h6l2 4H1z"/></svg>
        (650) 555-0143
      </li>
      <li>
        <svg viewBox="0 0 12 12" aria-hidden="true"><path d="M1 3h10v7H1z"/><path d="M1 3l5 4 5-4" fill="none" stroke="#fff" stroke-width="1"/></svg>
        dm@dorianmapl.es
      </li>
    </ul>
    <ul class="social">
      <li><span class="social__label">Chatline:</span> dmq527</li>
      <li><span class="social__label">Friendbook:</span> /Dorian.Maples</li>
      <li><span class="social__label">Workroll:</span> /in/dorianmaples</li>
    </ul>
    <div class="brand">
      <span class="brand__square"></span>
      <span class="brand__name">DM - management</span>
    </div>
  </section>

</main>
</body>
</html>
```